Custom Truck shop New Business Card design

double sided business card including my new logo, brand colors and picking a font I attached, clean and modern look. I attached the old card for some reference. and would like to include the picture of the white truck attached. I would also like to have it with one of my employees info as well. (same info except name and title Brin Tolvay Service Writer)

Dale Porvick
Owner

address
48310 E Calloway Ridge Rd S
STE 217
Marsh Hollow, CO 80219

phone 720-555-0184

email dale@brokenspurrigs.example

website brokenspurrgis.example

social @brokenspurrigs

Target Market(s)

men 18-60

Industry/Entity Type

Automotive

Contact Information for Business Card

Dale Porvick Owner address 48310 E Calloway Ridge Rd S STE 217 Marsh Hollow, CO 80219 phone 720-555-0184 email dale@brokenspurrigs.example website brokenspurrgis.example social @brokenspurrigs

Font styles to use
Other font styles liked:
• fonts attached

Requirements
Must have
• new logo, orange #FC68D, Charcoal #333333
Nice to have
• the white truck

```html
<!DOCTYPE html>
<html lang="en">
<head>
<meta charset="utf-8">
<title>Broken Spur Rigs – Business Card</title>
<link rel="stylesheet" href="https://fonts.googleapis.com/css2?family=Jost:wght@500&display=swap">
<style>
  :root {
    --brand-orange: #ea6d3c;
    --charcoal: #333333;
    --white: #ffffff;
    --photo-dark: #3c4540;
    --photo-mid: #8a9290;
    --photo-light: #dfe2e3;
  }
  html, body {
    margin: 0;
    padding: 0;
    overflow: hidden;
    background: #f2f2f2;
  }
  .card {
    position: relative;
    width: 1200px;
    height: 706px;
    overflow: hidden;
    background: var(--brand-orange);
    font-family: "Jost", "Futura", sans-serif;
    font-weight: 500;
    color: var(--charcoal);
  }
  .card-art {
    position: absolute;
    inset: 0;
    width: 1200px;
    height: 706px;
  }
  .holder-name {
    position: absolute;
    left: 56px;
    top: 47px;
    margin: 0;
    font-size: 41px;
    line-height: 44px;
    font-weight: 500;
    white-space: nowrap;
  }
  .name-underline {
    position: absolute;
    left: 56px;
    top: 97px;
    width: 153px;
    height: 3px;
    background: var(--charcoal);
    border-radius: 2px;
  }
  .contact-icon {
    position: absolute;
    left: 56px;
    width: 62px;
    height: 62px;
    border-radius: 50%;
    background: var(--charcoal);
  }
  .contact-icon svg {
    width: 62px;
    height: 62px;
    display: block;
  }
  .contact-line {
    position: absolute;
    left: 134px;
    margin: 0;
    font-size: 36px;
    line-height: 44px;
    white-space: nowrap;
  }
  .social-square {
    position: absolute;
    top: 587px;
    width: 48px;
    height: 48px;
    background: var(--charcoal);
  }
  .social-line {
    left: 243px;
    top: 589px;
  }
</style>
</head>
<body>
<div class="card">
  <svg class="card-art" viewBox="0 0 1004 591" preserveAspectRatio="none" aria-hidden="false">
    <defs>
      <linearGradient id="truck-photo-tone" x1="0" y1="0" x2="1" y2="1">
        <stop offset="0" stop-color="#4f5c50"/>
        <stop offset="0.35" stop-color="#7d827f"/>
        <stop offset="0.6" stop-color="#d9dcdd"/>
        <stop offset="1" stop-color="#3a3d40"/>
      </linearGradient>
    </defs>
    <polygon class="truck-photo" role="img"
      aria-label="Photo of a white lifted pickup truck with purple and gold suspension parked outside the shop"
      points="600,0 1004,0 1004,591 755,591 525,210" fill="url(#truck-photo-tone)"/>
    <polygon class="chevron-band" points="515,0 565,0 458,180 700,591 650,591 405,180" fill="#ffffff" fill-opacity="0.18"/>
    <polygon class="chevron-band" points="680,0 735,0 582,210 805,591 750,591 528,210" fill="#ffffff" fill-opacity="0.22"/>
  </svg>

  <h1 class="holder-name">Dale Porvick Owner</h1>
  <div class="name-underline"></div>

  <div class="contact-icon" style="top:230px">
    <svg viewBox="0 0 62 62" aria-hidden="true">
      <path d="M22 18c2-1 4 0 5 2l2 5c1 2 0 3-1 4l-2 2c2 4 5 7 9 9l2-2c1-1 2-2 4-1l5 2c2 1 3 3 2 5l-1 3c-1 2-3 3-5 3-12-1-22-11-23-23 0-2 1-4 3-5z" fill="#fff"/>
    </svg>
  </div>
  <p class="contact-line" style="top:239px">(720) 555-0184</p>

  <div class="contact-icon" style="top:307px">
    <svg viewBox="0 0 62 62" aria-hidden="true">
      <rect x="17" y="21" width="28" height="20" rx="2" fill="#fff"/>
      <path d="M18 23l13 10 13-10" fill="none" stroke="#333" stroke-width="2"/>
    </svg>
  </div>
  <p class="contact-line" style="top:316px">dale@brokenspurrigs.example</p>

  <div class="contact-icon" style="top:379px">
    <svg viewBox="0 0 62 62" aria-hidden="true">
      <circle cx="31" cy="31" r="12" fill="none" stroke="#fff" stroke-width="2.5"/>
      <path d="M21 25h20M21 37h20M31 19c-5 6-5 18 0 24M31 19c5 6 5 18 0 24" fill="none" stroke="#fff" stroke-width="2"/>
    </svg>
  </div>
  <p class="contact-line" style="top:388px">www.brokenspurrgis.example</p>

  <div class="contact-icon" style="top:453px">
    <svg viewBox="0 0 62 62" aria-hidden="true">
      <path d="M31 15c-6 0-11 5-11 11 0 8 11 21 11 21s11-13 11-21c0-6-5-11-11-11z" fill="#fff"/>
      <circle cx="31" cy="26" r="4" fill="#333"/>
    </svg>
  </div>
  <p class="contact-line" style="top:456px">48310 E Calloway Ridge Rd S STE<br>217 Marsh Hollow, CO 80219</p>

  <div class="social-square" style="left:56px"></div>
  <div class="social-square" style="left:120px"></div>
  <div class="social-square" style="left:180px"></div>
  <p class="contact-line social-line">social@brokenspurrgis.example</p>
</div>
</body>
</html>
```